Duck Egg label For Egg cartons

A "DUCK" needs to be designed for the Egg Carton label.
The design should contain the "DUCK" and also the lettering for the egg box.

please look at below attachments. that is an example of where we want to take this design. the Duck has to be an authentic design. we want the design to be modern and simple.

Logo Text

Corvel Farm

Requirements
Must have
• Lettering;
* Free Range
* Duck Eggs
* 12 eggs
* Corvel Farm

These are all the wordings to be used, you can use it how you think best fits the design.

```html
<!DOCTYPE html>
<html lang="en">
<head>
<meta charset="utf-8">
<title>Corvel Farm – Duck Eggs Carton Label</title>
<link rel="stylesheet" href="https://fonts.googleapis.com/css2?family=Great+Vibes&family=Open+Sans:wght@400;600&display=swap">
<style>
  :root {
    --page-bg: #f4f4f4;
    --label-bg: #3a3536;
    --label-ink: #ffffff;
    --art-tone-a: #4a4546;
    --art-tone-b: #5a5455;
  }
  * { margin: 0; padding: 0; box-sizing: border-box; }
  html, body {
    width: 1200px;
    height: 1200px;
    overflow: hidden;
    background: var(--page-bg);
  }
  .canvas {
    position: relative;
    width: 1200px;
    height: 1200px;
    display: flex;
    align-items: center;
    justify-content: center;
  }
  .carton-label {
    position: relative;
    width: 1080px;
    height: 330px;
    background: var(--label-bg);
    border-radius: 36px;
    color: var(--label-ink);
    overflow: hidden;
  }
  .brand-name {
    position: absolute;
    top: 28px;
    right: 64px;
    font-family: "Open Sans", sans-serif;
    font-weight: 600;
    font-size: 30px;
    letter-spacing: 0.01em;
  }
  .duck-illustration {
    position: absolute;
    left: 70px;
    top: 40px;
    width: 300px;
    height: 270px;
    border-radius: 20px;
    background: linear-gradient(160deg, var(--art-tone-b), var(--art-tone-a));
  }
  .product-lockup {
    position: absolute;
    left: 520px;
    top: 88px;
    width: 420px;
    text-align: center;
  }
  .product-title {
    font-family: "Great Vibes", cursive;
    font-weight: 400;
    font-size: 86px;
    line-height: 1;
  }
  .product-subtitle {
    font-family: "Great Vibes", cursive;
    font-size: 40px;
    line-height: 1;
    margin-top: 2px;
  }
  .product-count {
    font-family: "Open Sans", sans-serif;
    font-size: 22px;
    letter-spacing: 0.12em;
    margin-top: 20px;
  }
</style>
</head>
<body>
  <main class="canvas">
    <section class="carton-label">
      <div class="brand-name">Corvel Farm</div>
      <div class="duck-illustration" role="img" aria-label="White line drawing of a standing duck facing right"></div>
      <div class="product-lockup">
        <h1 class="product-title">Duck Eggs</h1>
        <p class="product-subtitle">Free Range</p>
        <p class="product-count">12 EGGS</p>
      </div>
    </section>
  </main>
</body>
</html>
```